Global Expert Network Firm needs business card design

We need business card design for a new company based in Seoul, South Korea called 'Corwell Insight Partners'. We recruit industry experts covering all countries and connect our client and recruited expert by phone, face-to-face meetings and etc. We are a global expert network firm that is focused on delivering high-quality experts to our clients throughout the world. Our clients include multinational corporations, global consulting firms, private equity firms, venture capital firms, asset management companies.
We have made new logo and please find attachment.(Please use new logo)
Target Market(s)
Global Consulting Firms, Investment Firms, Private Equity Firms, Venture Capital Firms.
Industry/Entity Type
Recruitment
Contact Information for Business Card
We need two Languages (English and Korean Version).
The front is Korean and the back is English version.
[The back] [English]
Company Name: Corwell Insight Partners, Inc.
CEO Name: Derek Hwang
Address: #508, Daerim Bldg, 72 Mokdongseo-ro, Yangcheon-gu, Seoul, 07918, Korea
Tel. +82 2 847 1215
Fax. +82 2 761 4218
Mobile. +82 10 6284 1215
Email: derek@corwellip.com
Web: www.corwellip.com
[The front] [Korean] => Described in same order as English version.
회사명: 코웰인사이트파트너스(주)
대표이사: 황도윤
주소: 서울시 양천구 목동서로 72 대림빌딩 508호
Tel. 02 847 1215
Fax. 02 761 4218
Mobile. 010 6284 1215
Web: www.corwellip.com

```html
<!DOCTYPE html>
<html lang="ko">
<head>
<meta charset="utf-8">
<title>Corwell Insight Partners — Business Card</title>
<link href="https://fonts.googleapis.com/css2?family=Quicksand:wght@400;500;700&family=Poppins:wght@400;600&family=Noto+Sans+KR:wght@300;400&display=swap" rel="stylesheet">
<style>
  :root {
    --bg: #d7dade;
    --card: #ffffff;
    --ink: #1e1e22;
    --navy: #1f3b8c;
    --rule: #2a2a2e;
  }
  * { margin: 0; padding: 0; box-sizing: border-box; }
  html, body { width: 1200px; height: 900px; overflow: hidden; }
  body { background: var(--bg); position: relative; font-family: "Quicksand", sans-serif; color: var(--ink); }

  .card {
    position: absolute; left: 300px; width: 600px; height: 340px;
    background: var(--card); border-radius: 24px;
    box-shadow: 0 6px 18px rgba(0,0,0,0.12);
  }
  .card--front { top: 60px; }
  .card--back { top: 500px; }

  .divider { position: absolute; left: 0; top: 0; width: 600px; height: 340px; pointer-events: none; }

  .wordmark {
    position: absolute; font-family: "Quicksand", sans-serif; font-weight: 700;
    color: var(--navy); line-height: 1.05; letter-spacing: 0.5px;
  }
  .wordmark-dot { display: inline-block; width: 12px; height: 12px; background: var(--navy); margin-right: 8px; vertical-align: 2px; }

  /* Korean front */
  .card--front .wordmark { left: 42px; top: 112px; font-size: 26px; }
  .company-ko { position: absolute; left: 42px; top: 184px; font-family: "Noto Sans KR", sans-serif; font-size: 15px; font-weight: 400; }
  .name-ko { position: absolute; right: 46px; top: 44px; text-align: center; font-family: "Noto Sans KR", sans-serif; }
  .name-ko .name { font-size: 28px; font-weight: 300; letter-spacing: 18px; margin-right: -18px; }
  .name-ko .title { font-size: 13px; display: flex; justify-content: space-between; margin-top: 2px; padding: 0 2px; }

  .contact { position: absolute; font-size: 12.5px; line-height: 1.55; font-weight: 500; }
  .card--front .contact { left: 312px; top: 168px; }
  .contact .rule { border-top: 1.2px solid var(--rule); margin: 8px 0 6px; width: 250px; }
  .contact .addr-ko { font-family: "Noto Sans KR", sans-serif; font-size: 12px; font-weight: 400; }

  /* English back */
  .name-en { position: absolute; left: 44px; top: 38px; }
  .name-en .name { font-family: "Poppins", sans-serif; font-weight: 600; font-size: 24px; letter-spacing: -0.5px; }
  .name-en .title { font-size: 14px; margin-left: 62px; }
  .card--back .contact { left: 44px; top: 140px; }
  .card--back .wordmark { right: 40px; bottom: 40px; font-size: 32px; text-align: right; }
</style>
</head>
<body>

<section class="card card--front" aria-label="Front, Korean">
  <svg class="divider" viewBox="0 0 600 340" aria-hidden="true">
    <line x1="296" y1="118" x2="276" y2="252" stroke="var(--rule)" stroke-width="1.2"/>
  </svg>
  <div class="wordmark"><span class="wordmark-dot"></span>Corwell Insight<br>Partners</div>
  <div class="company-ko">코웰인사이트파트너스(주)</div>
  <div class="name-ko">
    <div class="name">황도윤</div>
    <div class="title"><span>대표</span><span>이사</span></div>
  </div>
  <div class="contact">
    <div>Tel. 02 847 1215 | Fax. 02 761 4218</div>
    <div>Mobile. 010 6284 1215</div>
    <div>Email: derek@corwellip.com</div>
    <div>Web: www.corwellip.com</div>
    <div class="rule"></div>
    <div class="addr-ko">서울시 양천구 목동서로 72 대림빌딩 508호</div>
  </div>
</section>

<section class="card card--back" aria-label="Back, English">
  <svg class="divider" viewBox="0 0 600 340" aria-hidden="true">
    <line x1="330" y1="150" x2="304" y2="300" stroke="var(--rule)" stroke-width="1.2"/>
  </svg>
  <div class="name-en">
    <div class="name">Derek Hwang</div>
    <div class="title">CEO</div>
  </div>
  <div class="contact">
    <div>Tel. +82 2 847 1215 | Fax. +82 2 761 4218</div>
    <div>Mobile. +82 10 6284 1215</div>
    <div>Email: derek@corwellip.com</div>
    <div>Web: www.corwellip.com</div>
    <div class="rule"></div>
    <div>#508, Daerim Bldg, 72 Mokdongseo-ro,</div>
    <div>Yangcheon-gu, Seoul, 07918, Korea</div>
  </div>
  <div class="wordmark"><span class="wordmark-dot"></span>Corwell Insight<br>Partners</div>
</section>

</body>
</html>
```